Veterinary Business cards

Redesign Business Card

Information needed on Card:
Hours: Mon-Fri: 4pm -10PM; Sat- Sun- 10 AM- 5PM
Help@bayfernvet.com
www.bayfernvet.com
555-718-2946
4173 SE 19th Ave. okc, ok 73958
*No appointment necessary*

Optional:
Our tag line is "We're here when you need us" - If it fits on the cards.

```html
<!DOCTYPE html>
<html lang="en">
<head>
<meta charset="utf-8">
<title>Bayfern Vet Urgent Care – Business Card</title>
<link rel="stylesheet" href="https://fonts.googleapis.com/css2?family=Marcellus&family=Jost:wght@300;400;600&display=swap">
<style>
  :root {
    --orange: #d57c1d;
    --navy: #1d3f6e;
    --white: #ffffff;
    --backdrop: #4a4a4a;
    --card-w: 640px;
    --card-h: 366px;
  }
  * { box-sizing: border-box; margin: 0; padding: 0; }
  html, body { width: 1200px; height: 900px; overflow: hidden; }
  body {
    background: var(--backdrop);
    display: flex;
    flex-direction: column;
    align-items: center;
    justify-content: center;
    gap: 56px;
  }
  .card {
    position: relative;
    width: var(--card-w);
    height: var(--card-h);
    overflow: hidden;
  }

  /* Front */
  .card--front { background: var(--orange); color: var(--white); }
  .front__name {
    position: absolute; left: 0; right: 0; top: 96px;
    text-align: center;
    font-family: "Marcellus", serif;
    font-weight: 400;
    line-height: 1;
  }
  .front__name .brand {
    display: block;
    font-size: 62px; letter-spacing: 2px;
  }
  .front__name .sub {
    display: flex; align-items: center; gap: 14px;
    margin-top: 18px; padding-right: 100px;
    font-size: 24px; letter-spacing: 5px;
  }
  .front__name .sub::before, .front__name .sub::after {
    content: ""; height: 2px; background: var(--white);
  }
  .front__name .sub::before { flex: 1; }
  .front__name .sub::after { flex: 0 0 110px; }
  .tagline {
    position: absolute; left: 0; right: 0; top: 268px;
    display: flex; align-items: center; gap: 14px;
    font-family: "Marcellus", serif; font-size: 17px; letter-spacing: 1.5px;
  }
  .tagline::before, .tagline::after {
    content: ""; flex: 1; height: 2px; background: var(--white);
  }
  .tagline::before { flex: 0 0 190px; }

  /* Back */
  .card--back { background: var(--white); }
  .back__name {
    position: absolute; left: 0; right: 0; top: 36px;
    text-align: center; color: var(--navy);
    font-family: "Marcellus", serif; font-weight: 400; line-height: 1;
  }
  .back__name .brand { display: block; font-size: 46px; letter-spacing: 2px; }
  .back__name .sub {
    display: flex; align-items: center; justify-content: center; gap: 10px;
    margin-top: 8px; font-size: 18px; letter-spacing: 4px;
  }
  .back__name .sub::before, .back__name .sub::after {
    content: ""; width: 70px; height: 2px; background: var(--navy);
  }
  .contact {
    position: absolute; left: 318px; top: 150px;
    list-style: none;
    font-family: "Jost", sans-serif; font-weight: 300;
    font-size: 17px; color: var(--navy); line-height: 1.5;
  }
  .contact li { display: flex; align-items: center; gap: 7px; }
  .contact svg { width: 14px; height: 14px; flex: none; }
  .hours {
    position: absolute; left: 64px; top: 190px;
    font-family: "Jost", sans-serif; color: var(--navy);
    font-size: 15px; line-height: 1.45;
  }
  .hours__title { color: var(--orange); font-weight: 600; font-size: 19px; }
  .hours b { font-weight: 600; }
  .no-appointment {
    position: absolute; left: 0; right: 0; top: 300px;
    display: flex; align-items: center; gap: 12px;
    font-family: "Marcellus", serif; font-size: 19px; letter-spacing: 1.5px;
    color: var(--navy);
  }
  .no-appointment::before, .no-appointment::after {
    content: ""; flex: 1; height: 2px; background: var(--orange);
  }
</style>
</head>
<body>
  <section class="card card--front" aria-label="Card front">
    <h1 class="front__name">
      <span class="brand">BAYFERN VET</span>
      <span class="sub">URGENT CARE</span>
    </h1>
    <p class="tagline">WE'RE HERE WHEN YOU NEED US</p>
  </section>

  <section class="card card--back" aria-label="Card back">
    <h2 class="back__name">
      <span class="brand">BAYFERN VET</span>
      <span class="sub">URGENT CARE</span>
    </h2>

    <ul class="contact">
      <li>
        <svg viewBox="0 0 14 14" aria-hidden="true"><circle cx="7" cy="7" r="7" fill="var(--orange)"/><path d="M4.5 3.5l1.5 0 .6 1.8-1 .7a5 5 0 0 0 2.4 2.4l.7-1 1.8.6v1.5c-3.5.3-6.3-2.5-6-6z" fill="var(--white)"/></svg>
        555-718-2946
      </li>
      <li>
        <svg viewBox="0 0 14 14" aria-hidden="true"><circle cx="7" cy="7" r="7" fill="var(--orange)"/><rect x="3.5" y="4.5" width="7" height="5" fill="none" stroke="var(--white)" stroke-width="1"/><path d="M3.5 4.5L7 7.3l3.5-2.8" fill="none" stroke="var(--white)" stroke-width="1"/></svg>
        Help@bayfernvet.com
      </li>
      <li>
        <svg viewBox="0 0 14 14" aria-hidden="true"><circle cx="7" cy="7" r="7" fill="var(--orange)"/><circle cx="7" cy="7" r="3.8" fill="none" stroke="var(--white)" stroke-width="0.9"/><path d="M3.2 7h7.6M7 3.2c-2 2.2-2 5.4 0 7.6M7 3.2c2 2.2 2 5.4 0 7.6" fill="none" stroke="var(--white)" stroke-width="0.8"/></svg>
        www.bayfernvet.com
      </li>
      <li>
        <svg viewBox="0 0 14 14" aria-hidden="true"><circle cx="7" cy="7" r="7" fill="var(--orange)"/><path d="M3.5 7.2L7 4l3.5 3.2H9.5V10h-5V7.2z" fill="var(--white)"/></svg>
        4173 SE 19th Ave. okc, ok 73958
      </li>
    </ul>

    <div class="hours">
      <p class="hours__title">HOURS:</p>
      <p><b>MON - FRI</b> - 4PM - 10PM</p>
      <p><b>SAT- SUN</b> - 10 AM - 5PM</p>
    </div>

    <p class="no-appointment">*NO APPOINTMENT NECESSARY*</p>
  </section>
</body>
</html>
```